Software engineering company needs business card

I need a cool business card. Company: Soft Belan Brindlewood Ave 41 58207 Sincity Name: Gerald Vanholt CEO / Managing Director & Owner

```html
<!DOCTYPE html>
<html lang="en">
<head>
<meta charset="utf-8">
<title>Soft Belan – Business Card</title>
<link href="https://fonts.googleapis.com/css2?family=Open+Sans:wght@400;600;700&display=swap" rel="stylesheet">
<style>
  :root {
    --backdrop: #1f1f1f;
    --card: #ffffff;
    --green: #8dc63f;
    --charcoal: #4b4c4e;
    --text-grey: #666666;
    --text-dark: #3f4042;
  }
  * { margin: 0; padding: 0; box-sizing: border-box; }
  html, body {
    width: 1200px; height: 1000px; overflow: hidden;
    background: var(--backdrop);
    font-family: "Open Sans", Arial, sans-serif;
  }
  .card {
    position: absolute; left: 415px; top: 160px;
    width: 370px; height: 690px;
    background: var(--card);
    border-radius: 16px;
    overflow: hidden;
  }
  .brand-top {
    position: absolute; top: 78px; left: 0; width: 100%;
    text-align: center;
    font-size: 44px; font-weight: 700; line-height: 56px;
    color: var(--text-dark);
  }
  .name-band {
    position: absolute; top: 218px; left: 0; width: 100%; height: 66px;
    background: var(--green);
    text-align: center; padding-top: 6px;
  }
  .name-band .person {
    font-size: 29px; font-weight: 700; color: #fff; line-height: 34px;
  }
  .name-band .role {
    font-size: 15px; font-weight: 600; color: var(--text-dark); line-height: 20px;
  }
  .address {
    position: absolute; top: 350px; left: 84px;
    font-size: 17px; line-height: 26px; color: var(--text-grey);
  }
  .contacts {
    position: absolute; top: 414px; left: 84px; list-style: none;
    font-size: 17px; color: var(--text-grey);
  }
  .contacts li { display: flex; align-items: center; height: 27px; }
  .contacts svg { width: 13px; height: 13px; margin-right: 18px; fill: var(--green); }
  .contacts .accent { color: var(--green); }
  .brand-bottom {
    position: absolute; top: 590px; left: 0; width: 100%;
    display: flex; justify-content: center; align-items: center; gap: 10px;
    font-size: 24px; font-weight: 600; line-height: 32px; color: var(--text-dark);
  }
  .brand-bottom .mark { width: 12px; height: 12px; border-radius: 50%; background: var(--green); }
  .footer-bar { position: absolute; bottom: 0; left: 0; width: 100%; height: 46px; display: flex; }
  .footer-bar .dark { width: 148px; background: var(--charcoal); }
  .footer-bar .gap { width: 3px; background: var(--card); }
  .footer-bar .light { flex: 1; background: var(--green); }
</style>
</head>
<body>
  <div class="card">
    <div class="brand-top">Soft Belan</div>

    <div class="name-band">
      <div class="person">GERALD VANHOLT</div>
      <div class="role">CEO / Geschaftsfuhrer &amp; Inhaber</div>
    </div>

    <div class="address">
      Brindlewood Ave 41<br>
      58207 Sincity
    </div>

    <ul class="contacts">
      <li>
        <svg viewBox="0 0 24 24"><path d="M6.6 10.8a15.1 15.1 0 0 0 6.6 6.6l2.2-2.2a1 1 0 0 1 1-.25 11.4 11.4 0 0 0 3.6.57 1 1 0 0 1 1 1V20a1 1 0 0 1-1 1A17 17 0 0 1 3 4a1 1 0 0 1 1-1h3.5a1 1 0 0 1 1 1c0 1.25.2 2.45.57 3.57a1 1 0 0 1-.25 1z"/></svg>
        +000 555 218 304
      </li>
      <li>
        <svg viewBox="0 0 24 24"><path d="M2 5h20v14H2z M2 5l10 8 10-8" fill="none" stroke="#8dc63f" stroke-width="2.5"/><path d="M2 5h20L12 13z"/></svg>
        gerald@softbelan.com
      </li>
      <li>
        <svg viewBox="0 0 24 24"><circle cx="12" cy="12" r="10" fill="none" stroke="#8dc63f" stroke-width="2"/><ellipse cx="12" cy="12" rx="4.5" ry="10" fill="none" stroke="#8dc63f" stroke-width="2"/><path d="M2 12h20" stroke="#8dc63f" stroke-width="2"/></svg>
        www.<span class="accent">softbelan</span>.com
      </li>
    </ul>

    <div class="brand-bottom"><span class="mark"></span>Soft Belan</div>

    <div class="footer-bar">
      <div class="dark"></div><div class="gap"></div><div class="light"></div>
    </div>
  </div>
</body>
</html>
```